Mail order Nursery needs banner for promoting perennials that compliment roses.

banner should be 1135 wide x165 tall. We have an existing one displayed but we are not happy with the way it is washed out. Use your creativity to give us something that pops. Would love to see some watercolor or some other form of image other than just words washed across a stock photo. Banner needs to read Perennial Companions for Roses or some variation of that. Colors need to compliment our current theme. You can view the page and banner I want to replace at www.meadowlarkbloomyard.com. The banner we want to replace has been uploaded to the pixel forum file drop box. Thanks for your help and I look forward to seeing what you guys come up with. EDIT: I don't think I was clear enough in by brief. This banner promotes the sale of plants that look good planted with roses. We are getting to many submissions that are using only roses as the backdrop. We are looking for different types of plants that you would grow in your garden to compliment your roses. Thanks for all your hard work.

Target Market(s)

Home owners between 30 and 65

Industry/Entity Type

Nursery

Colors
33a6d7
e667a6

Requirements
Must have
• Text promotion perennials that compliment roses.... does not have to be those exact words but get the point across
Should not have
• Stock Photos with simple text washed across it.

```html
<!DOCTYPE html>
<html lang="en">
<head>
<meta charset="utf-8">
<title>Perennial Companions for Roses – Banner Concepts</title>
<link href="https://fonts.googleapis.com/css2?family=Great+Vibes&family=Montserrat:wght@400&family=Noto+Serif:ital,wght@0,400;0,700;1,400&family=Open+Sans:wght@400&family=Roboto:wght@400&display=swap" rel="stylesheet">
<style>
:root{
  --stage:#464646;
  --wine:#8e1230;
  --rose-deep:#b8364f;
  --rose:#e07f90;
  --blush:#f8d9cf;
  --peach:#f3a06f;
  --leaf:#6f9a46;
  --pink:#e667a6;
  --blue:#33a6d7;
  --ink:#222;
  --body:#555;
  --muted:#777;
  --rule:#e6e6e6;
}
*{box-sizing:border-box;margin:0;padding:0}
html,body{width:927px;height:1200px;overflow:hidden;background:#fff}
body{position:relative;font-family:"Noto Serif",Georgia,serif;color:var(--body)}
.stage{position:absolute;left:0;top:0;width:927px;height:517px;background:var(--stage)}
.banner{position:absolute;left:42px;width:843px;height:123px;overflow:hidden}
.banner-art{position:absolute;inset:0;
  background:
    radial-gradient(ellipse 120px 70px at 110px 60px,rgba(168,30,64,.75),transparent 70%),
    radial-gradient(ellipse 90px 60px at 230px 90px,rgba(196,52,86,.7),transparent 70%),
    radial-gradient(ellipse 70px 45px at 30px 100px,rgba(150,20,50,.6),transparent 70%),
    radial-gradient(ellipse 110px 80px at 790px 70px,rgba(240,130,90,.8),transparent 70%),
    radial-gradient(ellipse 60px 40px at 830px 20px,rgba(110,150,70,.55),transparent 70%),
    radial-gradient(ellipse 50px 35px at 700px 110px,rgba(110,150,70,.45),transparent 70%),
    linear-gradient(90deg,#f3b9bf 0%,#f8dcd2 40%,#f6d3c6 62%,#f9d8c8 80%,#f6c2a8 100%)}
.script{position:absolute;left:0;width:100%;font-family:"Great Vibes",cursive;color:var(--wine);letter-spacing:2px;white-space:nowrap}
.sans{position:absolute;font-family:"Roboto",Arial,sans-serif;color:var(--wine);white-space:nowrap}
.b1{top:51px}
.b1 .script{left:346px;top:14px;width:auto;font-size:46px;line-height:1}
.b1 .sans{left:488px;top:66px;font-size:25px}
.b2{top:198px}
.b2 .script{left:346px;top:10px;width:auto;font-size:46px;line-height:1}
.b2 .sans{left:491px;top:58px;font-size:22px}
.details-btn{position:absolute;left:454px;top:91px;width:167px;height:36px;border-radius:5px 5px 0 0;background:#d5546f;color:#fff;font-family:"Roboto",Arial,sans-serif;font-size:16px;text-align:center;line-height:30px;letter-spacing:.5px}
.b3{top:346px}
.b3 .title{position:absolute;left:349px;top:22px;font-family:"Open Sans",Arial,sans-serif;font-size:33px;color:#fff;letter-spacing:1px;white-space:nowrap}
.b3 .script{color:#fff;left:471px;top:58px;width:auto;font-size:40px}
.b4{top:1061px;left:40px}
.b4 .script{left:346px;top:14px;width:auto;font-size:46px;line-height:1}
.b4 .sans{left:488px;top:66px;font-size:25px}

.topbar{position:absolute;left:0;top:517px;width:927px;height:34px;border-bottom:1px solid var(--rule)}
.account-links{position:absolute;left:44px;top:10px;display:flex;gap:5px;font-size:9px;color:#444;list-style:none}
.account-links li::before{content:"•";margin-right:4px;font-size:8px}
.account-links li:first-child::before{margin-right:6px}
.account-links li:last-child::before{content:"•"}
.currency{position:absolute;left:313px;top:10px;font-size:8px;color:#444;display:flex;align-items:center;gap:4px}
.flag{width:11px;height:7px;background:linear-gradient(#b22 0 50%,#fff 50%);border:1px solid #999}
.search{position:absolute;left:620px;top:6px;width:119px;height:21px;border:1px solid #ddd;font-size:8px;color:#999;padding:5px 7px}
.search svg{position:absolute;right:6px;top:5px}
.cart-btn{position:absolute;left:746px;top:6px;width:21px;height:21px;background:var(--pink)}
.cart-text{position:absolute;left:774px;top:12px;font-size:8px;color:#444}

.brand{position:absolute;left:42px;top:566px;width:114px;text-align:center;font-size:13px;line-height:15px;color:var(--blue);letter-spacing:1px}
.main-nav{position:absolute;left:264px;top:563px;display:flex;list-style:none;font-family:"Montserrat",Arial,sans-serif;font-size:9.5px;letter-spacing:1.8px;color:#222}
.main-nav li{padding:14px 11px 0}
.main-nav .active{color:var(--pink);border-top:2px solid var(--pink)}

.crumbs{position:absolute;left:40px;top:633px;font-size:9.5px;color:#222}
.crumbs .here{color:var(--pink)}
.page-title{position:absolute;left:40px;top:656px;font-size:13.5px;font-weight:400;color:var(--ink)}
.copy{position:absolute;left:40px;top:691px;width:850px;font-size:9.5px;line-height:13.4px}
.copy p{margin-bottom:8px}
.copy ul{margin:-2px 0 4px 22px}
.section-rule{position:absolute;left:40px;top:898px;width:848px;height:1px;background:#222}
.section-label{position:absolute;left:406px;top:892px;padding:0 8px;background:#fff;font-family:"Montserrat",Arial,sans-serif;font-size:10px;letter-spacing:2px;color:#222}
.post-meta{position:absolute;left:40px;top:928px;font-size:9.5px;font-style:italic;color:var(--muted)}
.post-title{position:absolute;left:40px;top:949px;font-size:9.5px;font-weight:700;color:var(--blue)}
.post-excerpt{position:absolute;left:40px;top:966px;width:200px;font-size:9.5px;line-height:13.4px}
.read-more{position:absolute;left:40px;top:1017px;font-size:9.5px;font-style:italic;color:var(--muted)}
</style>
</head>
<body>
<div class="stage"></div>

<section class="banner b1">
  <div class="banner-art" role="img" aria-label="Watercolor roses in deep pink on the left and peach roses with leaves on the right over a blush wash"></div>
  <div class="script">Perennial Companions</div>
  <div class="sans">for Roses</div>
</section>

<section class="banner b2">
  <div class="banner-art" role="img" aria-label="Watercolor roses in deep pink on the left and peach roses with leaves on the right over a blush wash"></div>
  <div class="script">Perennial Companions</div>
  <div class="sans">for Roses</div>
  <div class="details-btn">Details</div>
</section>

<section class="banner b3">
  <div class="banner-art" role="img" aria-label="Watercolor roses in deep pink on the left and peach roses with leaves on the right over a blush wash"></div>
  <div class="title">Perennial Companions</div>
  <div class="script">for Roses</div>
</section>

<header class="topbar">
  <ul class="account-links"><li>Log in</li><li>Register</li><li>My Account</li><li>Check Out</li><li>Wishlist</li></ul>
  <div class="currency"><svg width="8" height="8" viewBox="0 0 8 8"><circle cx="4" cy="4" r="3" fill="none" stroke="#555" stroke-width="2"/></svg><span class="flag"></span>USD ⌄</div>
  <div class="search">Search ...<svg width="10" height="10" viewBox="0 0 10 10"><circle cx="4" cy="4" r="3" fill="none" stroke="#000" stroke-width="1.5"/><line x1="6.2" y1="6.2" x2="9" y2="9" stroke="#000" stroke-width="1.6"/></svg></div>
  <div class="cart-btn"><svg width="21" height="21" viewBox="0 0 21 21"><path d="M5 6h2l2 7h7l1.5-5H8" fill="none" stroke="#fff" stroke-width="1.6"/><circle cx="10" cy="15.5" r="1" fill="#fff"/><circle cx="15" cy="15.5" r="1" fill="#fff"/></svg></div>
  <div class="cart-text">Cart: 0 items - $ 0.00</div>
</header>

<div class="brand">MEADOWLARK<br>BLOOMYARD</div>
<ul class="main-nav">
  <li>HOME</li><li>CATALOG</li><li>OUR BLOG</li><li class="active">ABOUT US</li><li>ORDERING INFO</li><li>WISH LIST</li><li>CONTACT US</li>
</ul>

<div class="crumbs">⌂ Home &nbsp;/&nbsp; <span class="here">About Us</span></div>
<h1 class="page-title">ABOUT US</h1>
<div class="copy">
  <p>I am typing this.... does it show up on the template page?... YES ...A great About Us page helps builds trust between you and your customers. The more content you provide about you and your business, the more confident people will be when purchasing from your store.</p>
  <p>Your About Us page might include:</p>
  <ul>
    <li>Who you are</li><li>Why you sell the items you sell</li><li>Where you are located</li><li>How long you have been in business</li><li>How long you have been running your online shop</li><li>Who are the people on your team</li><li>Contact information</li><li>Social links</li>
  </ul>
  <p>To edit the content on this page, go to the Pages section of your Storefront admin.</p>
</div>

<div class="section-rule"></div>
<div class="section-label">LASTEST ADVICE</div>
<div class="post-meta">November 18, 2015 / 0 comments</div>
<div class="post-title">First Post</div>
<p class="post-excerpt">This is your store’s blog. You can use it to talk about new product launches,...</p>
<div class="read-more">Read more &nbsp;⟶</div>

<section class="banner b4">
  <div class="banner-art" role="img" aria-label="Watercolor roses in deep pink on the left and peach roses with leaves on the right over a blush wash"></div>
  <div class="script">Perennial Companions</div>
  <div class="sans">for Roses</div>
</section>
</body>
</html>
```